Calder Ridge Minerals

Looking for a cool, glossy business card...white with our logo on one side and then the a smaller version of the logo on the other side (top left hand corner) and then the name and position of the person next to it, and then the office address and email address on the bottom left hand corner and the phone numbers & email address on the bottom right hand corner. I have the logo already...can pass it on when you're ready.

```html
<!DOCTYPE html>
<html lang="en">
<head>
<meta charset="UTF-8">
<title>Calder Ridge Minerals – Business Card</title>
<link href="https://fonts.googleapis.com/css2?family=Cinzel:wght@400;600&family=Open+Sans:wght@400&display=swap" rel="stylesheet">
<style>
  :root {
    --backdrop: #dfe2e7;
    --card: #ffffff;
    --navy: #1d2554;
    --navy-light: #33449c;
    --royal: #2f47b0;
    --red: #c4172c;
    --red-dark: #9e1020;
    --ink: #2a2a2e;
    --muted: #4a4a50;
  }
  * { box-sizing: border-box; margin: 0; padding: 0; }
  html, body {
    width: 1200px; height: 900px; overflow: hidden;
    background: var(--backdrop);
  }
  .stage {
    position: relative; width: 1200px; height: 900px;
  }
  .card {
    position: absolute; left: 290px;
    width: 620px; height: 354px;
    background: var(--card);
    border-radius: 4px;
    overflow: hidden;
    box-shadow: 0 10px 28px rgba(20, 26, 50, 0.25);
  }
  .card--front { top: 70px; }
  .card--back { top: 476px; }
  .card__waves { position: absolute; inset: 0; width: 100%; height: 100%; }

  /* Front */
  .brand {
    position: absolute; left: 210px; top: 150px;
    display: flex; align-items: center; gap: 12px;
    font-family: "Cinzel", serif; font-weight: 600;
    color: var(--ink); letter-spacing: 1px;
  }
  .brand__dot {
    width: 16px; height: 16px; border-radius: 50%;
    background: var(--royal);
  }
  .brand__name { font-size: 24px; line-height: 1; }

  /* Back */
  .brand--small { left: 28px; top: 26px; gap: 7px; }
  .brand--small .brand__dot { width: 9px; height: 9px; }
  .brand--small .brand__name { font-size: 12px; }

  .contact {
    position: absolute;
    font-family: "Open Sans", sans-serif; font-size: 11px;
    color: var(--muted);
  }
  .contact__row { display: flex; align-items: center; gap: 9px; height: 20px; }
  .contact__icon { width: 12px; height: 12px; flex: none; }
  .contact--office { left: 28px; top: 70px; }
  .contact--direct { right: 34px; top: 270px; text-align: right; }
  .contact--direct .contact__row { justify-content: flex-end; }

  .person {
    position: absolute; right: 40px; top: 92px; text-align: right;
    font-family: "Cinzel", serif;
  }
  .person__name { font-size: 30px; font-weight: 600; color: var(--ink); letter-spacing: 1px; }
  .person__role { font-size: 15px; color: var(--red); margin-top: 6px; }

  .star-row {
    position: absolute; left: 250px; top: 150px;
    width: 110px; height: 8px; border-radius: 4px;
    background: linear-gradient(90deg, var(--royal), var(--red));
    opacity: 0.55;
  }
</style>
</head>
<body>
<main class="stage">

  <section class="card card--front">
    <svg class="card__waves" viewBox="0 0 620 354" preserveAspectRatio="none" aria-hidden="true">
      <defs>
        <linearGradient id="front-navy" x1="0" y1="0" x2="1" y2="1">
          <stop offset="0" stop-color="#151c44"/>
          <stop offset="1" stop-color="#2c3c92"/>
        </linearGradient>
        <linearGradient id="front-red" x1="0" y1="0" x2="1" y2="0">
          <stop offset="0" stop-color="#d11c33"/>
          <stop offset="1" stop-color="#9e1020"/>
        </linearGradient>
      </defs>
      <path d="M0,150 C150,170 300,300 620,344 L620,354 L0,354 Z" fill="url(#front-red)"/>
      <path d="M0,140 C140,170 270,300 540,354 L0,354 Z" fill="#ffffff"/>
      <path d="M0,22 C130,10 200,200 320,280 C380,320 440,345 500,354 L0,354 Z" fill="url(#front-navy)"/>
      <path d="M0,326 C200,328 420,342 620,350 L620,354 L0,354 Z" fill="#ffffff"/>
      <path d="M0,332 C200,334 420,346 620,352 L620,354 L0,354 Z" fill="var(--royal)"/>
    </svg>
    <div class="brand">
      <span class="brand__dot"></span>
      <span class="brand__name">Calder Ridge Minerals</span>
    </div>
  </section>

  <section class="card card--back">
    <svg class="card__waves" viewBox="0 0 620 354" preserveAspectRatio="none" aria-hidden="true">
      <defs>
        <linearGradient id="back-navy" x1="0" y1="0" x2="1" y2="0">
          <stop offset="0" stop-color="#3448a8"/>
          <stop offset="1" stop-color="#1a2150"/>
        </linearGradient>
        <linearGradient id="back-red" x1="0" y1="0" x2="1" y2="0">
          <stop offset="0" stop-color="#9e1020"/>
          <stop offset="1" stop-color="#d11c33"/>
        </linearGradient>
      </defs>
      <path d="M0,118 C90,130 200,190 330,200 L330,204 C200,200 90,150 0,140 Z" fill="url(#back-red)"/>
      <path d="M0,140 C120,150 200,230 330,260 C400,276 450,300 500,354 L0,354 Z" fill="url(#back-navy)"/>
    </svg>

    <div class="brand brand--small">
      <span class="brand__dot"></span>
      <span class="brand__name">Calder Ridge Minerals</span>
    </div>

    <div class="contact contact--office">
      <div class="contact__row">
        <svg class="contact__icon" viewBox="0 0 12 12" aria-hidden="true">
          <circle cx="6" cy="6" r="5.5" fill="var(--red)"/>
          <path d="M0.8,6 H11.2 M6,0.8 C3.5,3 3.5,9 6,11.2 M6,0.8 C8.5,3 8.5,9 6,11.2" stroke="#fff" stroke-width="0.8" fill="none"/>
        </svg>
        <span>www.websitename.com</span>
      </div>
      <div class="contact__row">
        <svg class="contact__icon" viewBox="0 0 12 12" aria-hidden="true">
          <path d="M6,0.5 C3.5,0.5 2,2.3 2,4.3 C2,7 6,11.5 6,11.5 C6,11.5 10,7 10,4.3 C10,2.3 8.5,0.5 6,0.5 Z" fill="var(--red)"/>
          <circle cx="6" cy="4.3" r="1.5" fill="#fff"/>
        </svg>
        <span>Street, Area, City, Country</span>
      </div>
    </div>

    <div class="star-row" role="img" aria-label="Row of five small stars"></div>

    <div class="person">
      <div class="person__name">Evan Hale</div>
      <div class="person__role">Director</div>
    </div>

    <div class="contact contact--direct">
      <div class="contact__row">
        <span>123 456 7890</span>
        <svg class="contact__icon" viewBox="0 0 12 12" aria-hidden="true">
          <path d="M3,1 L5,3.5 L4,5 C5,7 6,8 7,9 L8.5,8 L11,10 L9.5,11.5 C5,11 1,7 0.5,2.5 Z" fill="var(--red)"/>
        </svg>
      </div>
      <div class="contact__row">
        <span>info@email.com</span>
        <svg class="contact__icon" viewBox="0 0 12 12" aria-hidden="true">
          <rect x="0.8" y="2.3" width="10.4" height="7.4" fill="none" stroke="var(--red)" stroke-width="1.1"/>
          <path d="M0.8,2.3 L6,6.6 L11.2,2.3" fill="none" stroke="var(--red)" stroke-width="1.1"/>
        </svg>
      </div>
    </div>
  </section>

</main>
</body>
</html>
```